Bright Stride Clinic helping older adults use exercise as medicine

We need a website for a start up company providing exercise physiology and physiotherapy clinical services for people with serious health conditions such as cancer, diabetes and many others This is an exculsive service with limited time. The 2 main objectives of the website are to create leads for appointments and provide education about the benefits of exercise ie stretches, strength training, cardio vascular improvement for people with health conditions.
Please not too medical in design more fitness and lifestyle... sell the promise, please sell happy fit active people.

Target Market(s)

40-70 year old adults both male and female interested in a healthy lifestyle, ie baby boomers moderate education level (finished high school minimum) rural/country people

Industry/Entity Type

Health

Number of Pages Required

4 page

Font styles to use
Serif
Sans Serif

Colors
f26f22
3176b5

Requirements
Must have
• Website must have a blog/education area and a members area with access to an exercise database (picture, description and video)

```html
<!DOCTYPE html>
<html lang="en">
<head>
<meta charset="utf-8">
<title>Bright Stride Clinic – Appointments</title>
<link rel="stylesheet" href="https://fonts.googleapis.com/css2?family=Open+Sans:wght@400;600;700&family=Noto+Serif:ital@1&display=swap">
<style>
  :root {
    --orange: #f26f22;
    --blue: #3176b5;
    --navy: #1f3a57;
    --text: #333333;
    --field: #ececec;
    --cell-grey: #e5e5e5;
    --muted: #a9a9a9;
    --footer: #fddc9f;
    --nav-line: #c9c9c9;
  }
  * { box-sizing: border-box; margin: 0; padding: 0; }
  html, body { width: 1176px; height: 1200px; overflow: hidden; background: #fff; }
  body { position: relative; font-family: "Open Sans", Arial, sans-serif; color: var(--text); }

  .header-art {
    position: absolute; left: 0; top: 0; width: 356px; height: 128px;
    background: linear-gradient(160deg, #f48a4c 0%, #f9c9a8 55%, #ffffff 100%);
  }
  .brand {
    position: absolute; right: 30px; top: 64px;
    font-size: 30px; font-weight: 700; color: var(--blue);
    display: flex; align-items: center; gap: 10px;
  }
  .brand .dot { width: 18px; height: 18px; border-radius: 50%; background: var(--orange); }

  .main-nav {
    position: absolute; left: 12px; top: 144px; width: 1162px; height: 57px;
    background: linear-gradient(#fafafa, #e9e9e9);
    border-bottom: 1px solid #d6d6d6;
    display: flex;
  }
  .main-nav a {
    display: flex; align-items: center; justify-content: center;
    font-size: 17px; color: var(--blue); text-decoration: none;
    border-right: 2px solid var(--nav-line); height: 100%;
  }
  .main-nav a.active { color: var(--orange); background: #fff; border-left: 2px solid var(--nav-line); }
  .nav-home { width: 144px; } .nav-appt { width: 161px; } .nav-blog { width: 206px; }
  .nav-ex { width: 167px; } .main-nav a.nav-contact { width: 190px; border-right: none; }

  .banner {
    position: absolute; left: 12px; top: 245px; width: 1162px; height: 206px;
    background: #eeeeef;
  }
  .banner-photo {
    position: absolute; left: 0; top: 0; width: 330px; height: 206px;
    background: linear-gradient(135deg, #f4f4f4 0%, #e2e2e2 55%, #f5a06b 80%, #f26f22 100%);
  }
  .banner-tagline {
    position: absolute; left: 540px; top: 55px;
    font-family: "Noto Serif", Georgia, serif; font-style: italic;
    font-size: 42px; line-height: 50px; color: var(--orange);
  }
  .banner-tagline span { display: block; padding-left: 86px; }
  .banner-shade {
    position: absolute; left: 12px; top: 451px; width: 1162px; height: 70px;
    background: linear-gradient(#e4e4e4, rgba(255,255,255,0));
  }

  .page-title { position: absolute; left: 26px; top: 528px; font-size: 31px; font-weight: 400; color: #3a3a3a; }

  .form-label { position: absolute; left: 23px; font-size: 18px; font-family: Arial, sans-serif; color: #222; }
  .field {
    position: absolute; left: 25px; width: 367px; height: 47px;
    background: var(--field); padding-left: 20px;
    display: flex; align-items: center; font-size: 18px; font-family: Arial, sans-serif; color: #111;
  }
  .field-select::after {
    content: ""; position: absolute; right: 18px; top: 20px;
    border-left: 8px solid transparent; border-right: 8px solid transparent; border-top: 9px solid #aaa;
  }
  .submit-button {
    position: absolute; left: 28px; top: 989px; width: 264px; height: 39px;
    background: var(--orange); color: #fff; border: none;
    font-family: "Open Sans", sans-serif; font-weight: 600; font-size: 16px;
    box-shadow: 2px 3px 3px rgba(0,0,0,.3);
  }

  .calendar-label { position: absolute; left: 436px; top: 615px; font-size: 17px; font-family: Arial, sans-serif; color: #222; }
  .calendar { position: absolute; left: 436px; top: 650px; width: 327px; }
  .calendar-head {
    height: 68px; border-radius: 8px 8px 0 0;
    background: linear-gradient(#2f4f72, var(--navy));
    color: #fff; display: flex; align-items: center; justify-content: space-between;
    padding: 0 20px; font-weight: 700; font-size: 19px;
  }
  .calendar-head svg { width: 12px; height: 16px; fill: #fff; }
  .weekdays, .week { display: grid; grid-template-columns: repeat(7, 1fr); }
  .weekdays { background: #b8b8b8; height: 32px; color: #fff; font-weight: 700; font-size: 17px; }
  .weekdays span, .week span { display: flex; align-items: center; justify-content: center; }
  .week { height: 46px; font-weight: 700; font-size: 18px; color: #333; }
  .week.shaded { background: var(--cell-grey); }
  .week .muted { color: var(--muted); font-weight: 600; }
  .week .taken { background: var(--orange); color: #333; }
  .week .chosen { background: var(--blue); color: #333; }
  .legend { position: absolute; left: 436px; top: 1003px; width: 327px; display: flex; justify-content: space-between; font-size: 16px; font-style: italic; color: #888; }
  .legend span { display: flex; align-items: center; gap: 8px; }
  .legend i { width: 14px; height: 14px; display: inline-block; }

  .corner-art {
    position: absolute; left: 866px; top: 793px; width: 294px; height: 308px;
    background: radial-gradient(circle at 55% 55%, rgba(242,111,34,.35), rgba(242,111,34,.12) 45%, rgba(255,255,255,0) 70%);
  }

  .site-footer {
    position: absolute; left: 0; top: 1101px; width: 1176px; height: 99px;
    background: var(--footer);
    display: flex; align-items: center; justify-content: space-between; padding: 0 30px 0 13px;
  }
  .footer-note { font-weight: 700; font-size: 19px; color: var(--blue); }
  .footer-social { font-weight: 700; font-size: 22px; color: #555; }
</style>
</head>
<body>
  <div class="header-art" role="img" aria-label="Decorative header wave illustration with a cheerful figure"></div>

  <div class="brand"><span class="dot"></span>Bright Stride Clinic</div>

  <nav class="main-nav">
    <a class="nav-home" href="#">Homepage</a>
    <a class="nav-appt active" href="#">Appointments</a>
    <a class="nav-blog" href="#">Healthy Blog</a>
    <a class="nav-ex" href="#">Exercises</a>
    <a class="nav-contact" href="#">Contact</a>
  </nav>

  <section class="banner">
    <div class="banner-photo" role="img" aria-label="Photo of a calendar page with a date circled by an orange marker"></div>
    <p class="banner-tagline">At Bright Stride...<span>you get the best</span></p>
  </section>
  <div class="banner-shade"></div>

  <h1 class="page-title">Make an Appointment online:</h1>

  <label class="form-label" style="top:620px">Choose medical department:</label>
  <div class="field field-select" style="top:656px">Physiotherapy</div>
  <label class="form-label" style="top:742px">Your full name:</label>
  <div class="field" style="top:779px">Maren Holt</div>
  <label class="form-label" style="top:862px">Your email address:</label>
  <div class="field" style="top:900px">maren.holt@email.com</div>
  <button class="submit-button">MAKE APPOINTMENT</button>

  <p class="calendar-label">Choose a date for the appointment:</p>
  <div class="calendar">
    <div class="calendar-head">
      <svg viewBox="0 0 12 16"><path d="M12 0 L0 8 L12 16 Z"/></svg>
      <span>JANUARY 2012</span>
      <svg viewBox="0 0 12 16"><path d="M0 0 L12 8 L0 16 Z"/></svg>
    </div>
    <div class="weekdays"><span>M</span><span>T</span><span>W</span><span>T</span><span>F</span><span>S</span><span>S</span></div>
    <div class="week shaded"><span class="muted">31</span><span>1</span><span>2</span><span>3</span><span>4</span><span>5</span><span>6</span></div>
    <div class="week"><span>7</span><span>8</span><span>9</span><span>10</span><span>11</span><span>12</span><span>13</span></div>
    <div class="week shaded"><span>14</span><span>15</span><span class="taken">16</span><span>17</span><span class="taken">18</span><span>19</span><span>20</span></div>
    <div class="week"><span>21</span><span>22</span><span>23</span><span>24</span><span>25</span><span>26</span><span class="chosen">27</span></div>
    <div class="week shaded"><span>28</span><span>29</span><span>30</span><span>31</span><span class="muted">1</span><span class="muted">2</span><span class="muted">3</span></div>
  </div>
  <div class="legend">
    <span><i style="background:var(--blue)"></i>your selection</span>
    <span><i style="background:var(--orange)"></i>not available</span>
  </div>

  <div class="corner-art" role="img" aria-label="Faint decorative illustration of a figure raising its arms under a sunburst"></div>

  <footer class="site-footer">
    <span class="footer-note">Bright Stride - 2014</span>
    <span class="footer-social">Neighbours</span>
  </footer>
</body>
</html>
```